ReDesign of Velmarix.example and Velmarix app

Velmarix:

Velmarix aims to be your own personal cloud of profile information with ability to share a part of it with others based on the consumer.

As we visit different sites and buy different products, apply for new jobs, on-board in a company or fill out a basic form at a doctors office, we end up entering the same information again and again albeit with some sections different based on where you are. For example, we enter some basic informaiton “AND” billing address on brindle, vs you enter some basic information “AND” work history on a job site.

What if you created a profile one time and then create justed avatars or keys to a combination of information and at different places use different keys to unlock that specific piece of information.

Use Case 1: Peter Hale applying for a job
Peter goes to task harbor, creates new login, enters where he lives, email, phone, then goes into the most tedious phase of entering work history. He realizes, he also needs to go to Quillrun.example and do the exact same thing and so on on any job site he visits in future.

With Velmarix
Peter goes to Velmarix, updates all his work history, personal information (No SSN or credit card). Now he creates a new “key” called “petersworkrequest” with a cryptic “keycode” and chooses to share personal information + work history for this key. He now goes to any job site to see a “VX” icon. He clicks on that, a pop-up box with key and keycode appears. He ONLY enters petersworkrequset and the keycode he had set, boom, all his work informaiton is auto-populated in task harbor. Immense savings in time for Peter.

Use Case 2: Sharing contact information
Peter meets a beautiful at a bar and thinks he needs to share his personal information but only has a 5 mintue window. He realizes, he has created a key named “Peter42” and has chosen to share his personal information only (no work information). She asks for contact number, he gives her is VX key. She pulls up VX app instead of contact list to add contact, plugs in Peter42 (and a key if peter decides to protect this key with a code) and boom, she has peters phone/email/picture (yes picture), chatterly blog and a contact is automatically created!!!!! She now can really associate this Peter from 8 other Peter’s in the bar!!

Use Case 3: Always stay connected
Peter is bored of Houston and decides to move to LA.He wants a local phone number for people to get in touch with them easily. But now he has to do the painful job of sending all his friends his updated number/contact address. If he had exchanged information with Velmarix key with his friends, his contact information with them is always in sync. TThe Velmarix app is intelligent to know that new information is available for the same profile key. As long as the passcode is the same, that information is automatically updated in the consumers contact list. Next time Peter’s friend picks up the phone, he just need so hit “DIAL”. The correct number is dialed. Along with that, his friends now also have his updated address information which he had shared with the key.

SECURITY
Anytime anyone views your profile using your profile key, you automatically get notified to your registered email address of someone pulling up your profile. If you think it’s suspicious, you can change the access code or set an access code to that public key.

where to go:
Go to http://velmarix.example
Register and play around with different views you can create for your profile with different access codes

Download
Velmarix app from pomelo appshelf or Vantor playshelf. We need a nice look and feel for the app as well.

Target Market(s)

students, careers, hiring companies, anyone starting online presence

Industry/Entity Type

Credit Card

Requirements
Must have

• convey message, simplistic, an app to consume data, always stay updated with friends emails etc
Nice to have
• logo should show a user and multiple facets of user for multiple consumers

```html
<!DOCTYPE html>
<html lang="en">
<head>
<meta charset="utf-8">
<title>Velmarix – Find People</title>
<link rel="stylesheet" href="https://fonts.googleapis.com/css2?family=Open+Sans:wght@400;700&family=Exo:wght@300;400&display=swap">
<style>
  :root {
    --bg-center: #efefef;
    --bg-mid: #cfcfcf;
    --bg-edge: #b3b3b3;
    --ink: #2b2b2b;
    --ink-soft: #3a3a3a;
    --brand-green: #4e8c2a;
    --brand-green-dark: #2f5c17;
    --field-top: #6e6e6e;
    --field-mid: #a8a8a8;
    --field-bottom: #b9b9b9;
    --btn-top: #78bf3c;
    --btn-bottom: #5a9a28;
    --white: #ffffff;
  }
  html, body {
    margin: 0;
    padding: 0;
    width: 1200px;
    height: 857px;
    overflow: hidden;
  }
  body {
    background: radial-gradient(ellipse 640px 520px at 600px 470px, var(--bg-center) 0%, var(--bg-mid) 60%, var(--bg-edge) 100%);
    font-family: "Open Sans", sans-serif;
    position: relative;
  }
  .brand {
    position: absolute;
    top: 219px;
    left: 497px;
    display: flex;
    align-items: center;
    gap: 9px;
  }
  .brand-mark {
    width: 42px;
    height: 42px;
    border-radius: 6px;
    background: linear-gradient(var(--brand-green), var(--brand-green-dark));
  }
  .brand-name {
    font-size: 26px;
    font-weight: 400;
    color: var(--ink);
    letter-spacing: 0.2px;
  }
  .search-panel {
    position: absolute;
    top: 314px;
    left: 400px;
    width: 400px;
  }
  .search-title {
    display: flex;
    justify-content: center;
    align-items: center;
    gap: 9px;
    height: 28px;
    font-family: "Exo", sans-serif;
    font-weight: 300;
    font-size: 18px;
    color: var(--ink-soft);
    margin-left: -30px;
  }
  .search-field {
    margin-top: 24px;
    display: block;
    width: 400px;
    height: 39px;
    box-sizing: border-box;
    border: none;
    border-radius: 20px;
    background: linear-gradient(var(--field-top) 0%, var(--field-mid) 30%, var(--field-bottom) 100%);
    box-shadow: inset 3px 2px 4px rgba(0,0,0,0.45);
    text-align: center;
    font-family: "Open Sans", sans-serif;
    font-size: 11px;
    color: var(--white);
    outline: none;
  }
  .search-field::placeholder { color: var(--white); opacity: 1; }
  .find-button {
    margin-top: 11px;
    display: block;
    width: 400px;
    height: 39px;
    border: none;
    border-radius: 20px;
    background: linear-gradient(var(--btn-top), var(--btn-bottom));
    font-family: "Exo", sans-serif;
    font-weight: 300;
    font-size: 20px;
    color: var(--white);
    cursor: pointer;
  }
</style>
</head>
<body>
  <header class="brand">
    <span class="brand-mark"></span>
    <span class="brand-name">Velmarix</span>
  </header>

  <main class="search-panel">
    <h1 class="search-title" style="margin-top:0;margin-bottom:0;">
      <svg width="20" height="18" viewBox="0 0 20 18" aria-hidden="true">
        <circle cx="7" cy="7" r="5" fill="none" stroke="#4a4a4a" stroke-width="2.4"/>
        <line x1="11" y1="11" x2="18" y2="16" stroke="#4a4a4a" stroke-width="4" stroke-linecap="round"/>
      </svg>
      Find People
    </h1>
    <input class="search-field" type="text" placeholder="Search by profil ID" aria-label="Search by profile ID">
    <button class="find-button" type="button">FIND</button>
  </main>
</body>
</html>
```